Business Card Design - Local Discount Club

Looking for a fun business card for a local discount club. One side should be the logo only and the other should be have :

Name
Title
Phone, Email
Website

```html
<!DOCTYPE html>
<html lang="en">
<head>
<meta charset="utf-8">
<title>The Harbor Perk Card – Business Card</title>
<link rel="stylesheet" href="https://fonts.googleapis.com/css2?family=Lato:wght@400;700;900&display=swap">
<style>
  :root {
    --backdrop: #e6e4e1;
    --card: #ffffff;
    --navy: #4a63b3;
    --sky: #6fcbe9;
    --leaf: #b5db8c;
    --ink: #4a63b3;
    --rule: #8aa86a;
  }
  * { box-sizing: border-box; margin: 0; padding: 0; }
  html, body {
    width: 1200px; height: 913px; overflow: hidden;
    background: var(--backdrop);
    font-family: "Lato", sans-serif;
  }
  .card {
    position: absolute; left: 240px;
    width: 720px; height: 411px;
    background: var(--card);
    box-shadow: 0 6px 18px rgba(0,0,0,.18);
    overflow: hidden;
  }
  .card--front { top: 26px; }
  .card--back { top: 476px; }

  .brand {
    display: flex; align-items: center; gap: 14px;
    color: var(--navy); font-weight: 900;
    letter-spacing: .5px; line-height: 1;
    white-space: nowrap;
  }
  .brand__dot { border-radius: 50%; background: var(--sky); flex: none; }

  .card--front .front-url {
    position: absolute; left: 0; right: 0; top: 140px;
    text-align: center; color: var(--navy);
    font-size: 15px; letter-spacing: 2px;
  }
  .card--front .brand {
    position: absolute; left: 0; right: 0; top: 178px;
    justify-content: center; font-size: 46px;
  }
  .card--front .brand__dot { width: 26px; height: 26px; }

  .back-art { position: absolute; inset: 0; width: 720px; height: 411px; }
  .card--back .brand {
    position: absolute; left: 50px; top: 100px; font-size: 30px;
  }
  .card--back .brand__dot { width: 18px; height: 18px; }

  .person {
    position: absolute; right: 34px; top: 268px;
    color: var(--ink); font-size: 19px;
    display: flex; align-items: baseline; gap: 8px;
    white-space: nowrap;
  }
  .person__name { font-weight: 900; font-size: 24px; letter-spacing: 1px; }
  .person__sep { font-size: 24px; }
  .rule { position: absolute; height: 1px; background: var(--rule); }
  .rule--top { left: 330px; right: 30px; top: 306px; }
  .rule--bottom { left: 60px; right: 30px; top: 378px; }
  .contacts {
    position: absolute; right: 30px; top: 330px;
    display: flex; align-items: center; gap: 8px;
    color: var(--ink); font-size: 17px;
    white-space: nowrap;
  }
  .contacts__icon { width: 15px; height: 15px; flex: none; }
</style>
</head>
<body>

<section class="card card--front" aria-label="Card front">
  <p class="front-url">www.harborperkcard.com</p>
  <div class="brand"><span class="brand__dot"></span>The Harbor Perk Card</div>
</section>

<section class="card card--back" aria-label="Card back">
  <svg class="back-art" viewBox="0 0 720 411" aria-hidden="true">
    <polygon fill="var(--navy)" points="0,300 0,312 720,160 720,148"/>
    <polygon fill="var(--sky)"  points="0,312 0,322 720,170 720,160"/>
    <polygon fill="var(--leaf)" points="0,322 0,330 720,178 720,170"/>
    <polygon fill="var(--leaf)" points="0,340 0,411 720,411 720,188"/>
  </svg>

  <div class="brand"><span class="brand__dot"></span>The Harbor Perk Card</div>

  <div class="person">
    <span class="person__title">Director</span>
    <span class="person__sep">|</span>
    <span class="person__name">DANA MERCER</span>
  </div>
  <div class="rule rule--top"></div>

  <div class="contacts">
    <span>www.harborperkcard.com</span>
    <svg class="contacts__icon" viewBox="0 0 16 16" aria-hidden="true"><circle cx="8" cy="8" r="6.5" fill="none" stroke="var(--ink)" stroke-width="1.5"/><path d="M1.5 8h13M8 1.5c-3 3.5-3 9.5 0 13M8 1.5c3 3.5 3 9.5 0 13" fill="none" stroke="var(--ink)" stroke-width="1.2"/></svg>
    <span>|</span>
    <span>hello@harborperkcard.com</span>
    <svg class="contacts__icon" viewBox="0 0 16 16" aria-hidden="true"><rect x="1" y="3" width="14" height="10" rx="1" fill="var(--ink)"/><path d="M1.5 3.8 8 9l6.5-5.2" fill="none" stroke="#fff" stroke-width="1.3"/></svg>
    <span>|</span>
    <span>555-014-2273</span>
    <svg class="contacts__icon" viewBox="0 0 16 16" aria-hidden="true"><path d="M4 2l2.5 3-1.5 1.5c.8 1.8 2.2 3.2 4 4L10.5 9 13.5 11.5 12 14C6.5 13.5 2.5 9.5 2 4z" fill="var(--ink)"/></svg>
  </div>
  <div class="rule rule--bottom"></div>
</section>

</body>
</html>
```